Harbourline Coldworks Tri-fold Information Brochure

Looking for a sleek, clean and professional design for a tri-fold brochure so people can learn about Harbourline Coldworks, understand what Cryotherapy is, and what it can do for them.

Will be printed using pressly cards (dimensions provided on their website say the tri-fold will be 8.5" x 11" {279 x 216 mm})

Include out website: www.harbourlinecoldworks.ca:
social media handles
Facebook and Instagram: @Harbourlinecoldworks
Twitter: @HarbCold

Sections- Below I will provide copyright and sections that must be included in the brochure. The title of the sections can be modified (lengthened or shortened) to provide the best look.

Benefits:
Pain Management
Injury Therapy
Rapid Recovery
Performance
Metabolic Boost
Immunity Boost
Anti-Aging
Skin Rejevenation

Applications:
Athletic Performance
Post-surgical Recovery
Musculosketetal Injuries
Rheumatoid Arthritis
Caloric Burn
Skin Disorders
Autoimmune and Other Inflammatory Disorders

Used by professional athletes: logos for the PBL, GFA, RKA, DBU, KSF, WJX, TWE Circuit

As seen on TV: Logos for Dr. Quill Hour, Bright Dawn Daily, TVK, WJR Games, Wanderlight Network, QP, The Healers, KRT Report

Customized Treatment Protocols

Just 3 Minutes

FAQs

How Does Cryotherapy Work?
Whole body skin exposure to the ultra-low temperatures -145°C to -165°C (-229°F to -265°F) triggers a systemic anti-inflammatory response that activates organs, muscles, joints, and skin to heal and repair themselves. The result is a dramatic increase in circulation, metabolism, tissue repair, detoxification and immune function.

Is it comfortable?
The treatment is short and the cold air has no moisture present, so it's very tolerable and much easier to do compared to an ice bath or cold shower. Towards the end of the treatment, you may get a "pins and needles" sensation that disappears immediately after the treatment.

Is it safe?
No, the liquid nitrogen that is used as a chilling agent does not come into contact with your skin. Nitrogen is nontoxic, and nonflammable it comprises 78% of the air we breathe. A trained operator is always present during the treatment to control the temperature and monitor your comfort. There are no locks or latches on the door so you are able exit the cryochamber easily and quickly anytime.

How do I feel after a treatment?
the brisk exhilaration causes your brain to release high amounts of endorphin and norepinephrine, which make you feel good and focused. Most people report feeling energetic and full of like. The buoyant effects from each session peak after many hours and may last for weeks.

Target Market(s)

People that stay active and are looking to take advantage of the benefits of cryotherapy. People with chronic or acute conditions looking to accelerate and help with recovery and treatment.

Industry/Entity Type

Health And Wellness

Font styles to use
Sans Serif

Colors
ffffff
000000
57b5de

Requirements
Must have
• Use logo colors (white, black and blue) the shade of blue to be used must be as close to the logo's shade of blue as possible.
• A picture of the machine that has been provided or a picture of a similar looking machine from online.
Nice to have
• Mountains or mist
• a person running/being active
• a person doing yoga or a women boxing
• a picture signifying joint pain

```html
<!DOCTYPE html>
<html lang="en">
<head>
<meta charset="utf-8">
<title>Harbourline Coldworks – Tri-fold Brochure</title>
<link rel="stylesheet" href="https://fonts.googleapis.com/css2?family=Open+Sans:wght@400;600&family=Oswald:wght@500&family=Roboto:wght@400;500&family=Roboto+Condensed:wght@300;400;700&family=Montserrat:wght@700&family=Kaushan+Script&display=swap">
<style>
  :root{
    --blue:#3fa9e0;
    --ink:#262626;
    --charcoal:#2b2b2d;
    --paper:#ffffff;
    --mist:#eef6fb;
    --sand:#ead9c2;
    --gold:#9c7a3c;
    --label:#444;
  }
  *{box-sizing:border-box;margin:0;padding:0}
  html,body{width:1200px;height:1200px;overflow:hidden;background:var(--paper)}
  body{position:relative;font-family:"Open Sans",sans-serif}

  .spread{position:absolute;width:636px;height:490px;display:flex;box-shadow:16px 14px 9px rgba(0,0,0,.55);background:var(--paper)}
  .spread--front{left:270px;top:68px}
  .spread--back{left:267px;top:623px}
  .panel{position:relative;height:100%;overflow:hidden}

  .fold-label{position:absolute;font-family:"Kaushan Script",cursive;font-size:25px;color:var(--label)}
  .fold-label--front{left:928px;top:84px}
  .fold-label--back{left:944px;top:636px}

  /* spine band */
  .spine{width:82px;background:var(--ink);color:var(--paper)}
  .spine__mark{position:absolute;left:24px;top:38px;width:36px;height:28px;border:2px solid var(--paper)}
  .spine__name{position:absolute;left:24px;top:68px;writing-mode:vertical-rl;white-space:nowrap;font-family:"Roboto",sans-serif;font-weight:500;font-size:15.5px;line-height:19px;letter-spacing:.4px}
  .spine__tag{position:absolute;left:26px;top:254px;writing-mode:vertical-rl;white-space:nowrap;color:var(--blue);font-family:"Roboto Condensed",sans-serif;font-weight:700}
  .spine__protocol{font-size:11.5px;line-height:17px;letter-spacing:.3px}
  .spine__minutes{font-size:24px;line-height:25px}

  /* front panel 1 */
  .cover{width:211px;background:var(--mist)}
  .cover__visual{position:absolute;left:34px;top:48px;width:148px;height:398px;background:linear-gradient(90deg,#e6d5be,var(--sand))}
  .cover__brand{position:absolute;left:58px;top:216px;width:100px;height:62px;border:4px solid var(--ink);display:flex;align-items:center;justify-content:center;text-align:center;font-family:"Roboto",sans-serif;font-weight:500;font-size:11px;line-height:13px;color:var(--ink)}
  .cover__web{position:absolute;left:0;right:0;top:462px;text-align:center;font-family:"Montserrat",sans-serif;font-size:8.5px;color:#555}

  /* front panel 2 */
  .credits{width:214px;background:var(--blue);color:var(--paper)}
  .frame{position:absolute;border:3px solid var(--paper)}
  .frame--endorse{left:15px;top:33px;width:182px;height:189px;text-align:center;font-family:"Oswald",sans-serif;font-size:9.5px}
  .frame--contact{left:15px;top:274px;width:184px;height:189px}
  .endorse__title{margin-top:43px}
  .endorse__title--tv{margin-top:22px}
  .badge-row{display:flex;justify-content:center;gap:5px;margin-top:12px}
  .badge{background:var(--paper);border-radius:2px}
  .badge--sm{width:11px;height:12px}
  .badge--wide{width:20px;height:12px}
  .badge--tv{width:34px;height:20px}
  .tick-lines{position:absolute}
  .contact-list{list-style:none;position:absolute;left:24px;top:48px;font-size:8.5px}
  .contact-list li{display:flex;align-items:center;gap:14px;height:26px}
  .contact-list svg{width:21px;height:22px;flex:none}

  /* front panel 3 */
  .scenery{width:129px}
  .scenery__photo{position:absolute;inset:0;background:linear-gradient(175deg,#d3dbe2 0%,#9aa8b5 28%,#e6ebef 52%,#b9c4cc 75%,#dfe5ea 100%)}
  .scenery svg{position:absolute;inset:0}

  /* back panel 1 */
  .faq{width:213px;background:var(--charcoal);color:#e8e8e8}
  .faq__rule{position:absolute;left:17px;top:0;width:4px;height:453px;background:var(--gold)}
  .faq__photo{position:absolute;left:19px;top:0;width:151px;height:103px;background:linear-gradient(180deg,#3a6ea0,#7ea8cc 45%,#c9b7a6 70%,#5b7fa6)}
  .faq__title{position:absolute;left:24px;top:88px;font-family:"Oswald",sans-serif;font-size:10px;letter-spacing:2px;color:var(--paper)}
  .faq__body{position:absolute;left:10px;top:114px;width:196px}
  .faq__q{font-family:"Kaushan Script",cursive;font-size:9.5px;line-height:12px;color:var(--paper);display:flex;align-items:center;gap:3px;margin-top:7px}
  .faq__q:first-child{margin-top:0}
  .faq__q svg{width:11px;height:11px;flex:none}
  .faq__a{margin:5px 0 0 14px;font-size:6px;line-height:8.7px;color:#ddd}
  .faq__a p{text-indent:28px}
  .faq__web{position:absolute;left:38px;top:470px;width:123px;height:13px;background:var(--blue);color:var(--paper);font-family:"Montserrat",sans-serif;font-size:7.5px;text-align:center;line-height:13px}

  /* back panel 2 */
  .applications{width:213px;background:var(--blue);color:var(--paper)}
  .applications__wave{position:absolute;left:0;top:0}
  .shot{position:absolute;box-shadow:2px 3px 5px rgba(0,0,0,.45)}
  .shot--knee{left:110px;top:27px;width:99px;height:65px;background:linear-gradient(160deg,#c9b06a,#e9d9a2 40%,#7f8a3e)}
  .shot--gym{left:0;top:114px;width:100px;height:66px;background:linear-gradient(120deg,#2c3a4e,#6f8198 50%,#2b3340)}
  .shot--road{left:108px;top:217px;width:102px;height:61px;background:linear-gradient(180deg,#8e8a82,#c7ad86 45%,#4c4844)}
  .blurb{position:absolute;width:96px;font-size:4.6px;line-height:6.4px;color:#e8f4fb}
  .applications__title{position:absolute;left:0;right:0;top:310px;text-align:center;font-family:"Kaushan Script",cursive;font-size:24px;text-shadow:1px 2px 3px rgba(0,0,0,.45)}
  .applications__list,.benefits__list{list-style:none;position:absolute;left:0;right:0;text-align:center;font-family:"Roboto Condensed",sans-serif}
  .applications__list{top:355px;font-size:10px;line-height:13.5px;font-weight:300;text-shadow:1px 1px 2px rgba(0,0,0,.45)}

  /* back panel 3 */
  .benefits{width:129px;background:var(--paper);color:var(--ink)}
  .benefits__brand{position:absolute;left:11px;top:30px;display:flex;align-items:center;gap:4px;font-family:"Roboto",sans-serif;font-weight:500;font-size:8.5px;line-height:9.5px}
  .benefits__brand i{display:block;width:31px;height:20px;border:2px solid var(--blue)}
  .benefits__title{position:absolute;left:6px;top:82px;font-family:"Kaushan Script",cursive;font-size:29px;text-shadow:2px 3px 3px rgba(0,0,0,.35)}
  .benefits__list{top:175px;font-size:11.2px;line-height:15.4px;font-weight:300;color:#1e1e1e;text-shadow:1px 1px 1px rgba(0,0,0,.2)}
  .benefits__machine{position:absolute;left:0;top:326px;width:129px;height:164px;background:linear-gradient(90deg,#9fa6b1,#d9dde2 35%,#b9bec6 60%,#e5e6e8)}
</style>
</head>
<body>

<div class="fold-label fold-label--front">Front fold</div>
<div class="fold-label fold-label--back">Back fold</div>

<!-- FRONT -->
<section class="spread spread--front">
  <div class="panel cover">
    <div class="cover__visual" role="img" aria-label="Illustration of a cryotherapy chamber door"></div>
    <div class="cover__brand">Harbourline Coldworks</div>
    <div class="cover__web">www.yourwebsite.com</div>
  </div>

  <div class="panel credits">
    <svg class="tick-lines" style="left:6px;top:106px" width="5" height="118" viewBox="0 0 5 118"><rect x="1" y="0" width="3" height="62" fill="#fff"/><rect x="1" y="70" width="3" height="10" fill="#fff"/><rect x="1" y="86" width="3" height="10" fill="#fff"/><rect x="1" y="101" width="3" height="8" fill="#fff"/><circle cx="2.5" cy="115" r="2.2" fill="#fff"/></svg>
    <div class="frame frame--endorse">
      <div class="endorse__title">Used by professional athletes</div>
      <div class="badge-row"><span class="badge badge--sm"></span><span class="badge badge--sm"></span><span class="badge badge--sm"></span><span class="badge badge--wide"></span></div>
      <div class="endorse__title endorse__title--tv">As seen on TV</div>
      <div class="badge-row"><span class="badge badge--tv"></span><span class="badge badge--tv"></span><span class="badge badge--tv"></span></div>
    </div>
    <svg class="tick-lines" style="left:203px;top:275px" width="5" height="118" viewBox="0 0 5 118"><rect x="1" y="0" width="3" height="34" fill="#fff"/><rect x="1" y="62" width="3" height="28" fill="#fff"/><rect x="1" y="96" width="3" height="10" fill="#fff"/><circle cx="2.5" cy="114" r="2.2" fill="#fff"/></svg>
    <div class="frame frame--contact">
      <ul class="contact-list">
        <li><svg viewBox="0 0 22 24"><polygon points="11,1 21,6.5 21,17.5 11,23 1,17.5 1,6.5" fill="none" stroke="#fff"/><path d="M11 6a4 4 0 0 1 4 4c0 3-4 7-4 7s-4-4-4-7a4 4 0 0 1 4-4z" fill="none" stroke="#fff"/><circle cx="11" cy="10" r="1.4" fill="#fff"/></svg>2345 St, Your Address, City</li>
        <li><svg viewBox="0 0 22 24"><polygon points="11,1 21,6.5 21,17.5 11,23 1,17.5 1,6.5" fill="none" stroke="#fff"/><path d="M7.5 7.5l2 -0.5 1.2 2.6-1.3 1c.6 1.4 1.6 2.4 3 3l1-1.3 2.6 1.2-.5 2c-4.5.2-8.2-3.5-8-8z" fill="none" stroke="#fff"/></svg>555-014-2270</li>
        <li><svg viewBox="0 0 22 24"><polygon points="11,1 21,6.5 21,17.5 11,23 1,17.5 1,6.5" fill="none" stroke="#fff"/><rect x="6" y="8" width="10" height="8" fill="none" stroke="#fff"/><path d="M6 8l5 4.5L16 8M6 16l3.5-3.5M16 16l-3.5-3.5" fill="none" stroke="#fff"/></svg>yourdesign@email.com</li>
        <li><svg viewBox="0 0 22 24"><polygon points="11,1 21,6.5 21,17.5 11,23 1,17.5 1,6.5" fill="none" stroke="#fff"/><circle cx="11" cy="12" r="5" fill="none" stroke="#fff"/><path d="M6 12h10M11 7c-2.4 3-2.4 7 0 10M11 7c2.4 3 2.4 7 0 10" fill="none" stroke="#fff"/></svg>www.yourline.com</li>
      </ul>
    </div>
  </div>

  <div class="panel scenery">
    <div class="scenery__photo" role="img" aria-label="Photo of a snowy mountain peak with mist and a pine tree"></div>
    <svg width="129" height="490" viewBox="0 0 129 490">
      <polygon points="0,250 129,470 129,490 0,490" fill="#3fa9e0" opacity=".45"/>
      <g stroke="#7cc6ec" stroke-width="1" opacity=".8">
        <line x1="0" y1="275" x2="110" y2="490"/><line x1="0" y1="300" x2="98" y2="490"/><line x1="0" y1="325" x2="85" y2="490"/><line x1="0" y1="350" x2="72" y2="490"/>
      </g>
      <polygon points="129,378 129,490 22,490" fill="#3fa9e0"/>
    </svg>
  </div>

  <div class="panel spine">
    <div class="spine__mark"></div>
    <div class="spine__name">HARBOURLINE<br>COLDWORKS</div>
    <div class="spine__tag"><span class="spine__protocol">CUSTOMIZE TREATMENT PROTOCOL</span><br><span class="spine__minutes">JUST 3 MINUTE</span></div>
  </div>
</section>

<!-- BACK -->
<section class="spread spread--back">
  <div class="panel faq">
    <div class="faq__rule"></div>
    <div class="faq__photo" role="img" aria-label="Photo of a client inside a cryotherapy chamber"></div>
    <div class="faq__title">FAQS</div>

    <div class="faq__body">
      <div class="faq__q"><svg viewBox="0 0 12 12"><circle cx="6" cy="6" r="5" fill="none" stroke="#fff"/><path d="M3.5 6.2l1.8 1.8 3.3-3.6" fill="none" stroke="#fff"/></svg>How Does Cryotherapy Work?</div>
      <div class="faq__a"><p>Whole body skin exposure to the ultra-low temperatures -145°C to -165°C (-229°F to -265°F) triggers a systemic anti-inflammatory response that activates organs, muscles, joints, and skin to heal and repair themselves. The result is a dramatic increase in circulation, metabolism, tissue repair, detoxification and immune function.</p></div>

      <div class="faq__q"><svg viewBox="0 0 12 12"><path d="M1 9h10M2 9l3-4 2 2 3-3" fill="none" stroke="#fff" stroke-width="1.4"/></svg>Is it comfortable?</div>
      <div class="faq__a"><p>The treatment is short and the cold air has no moisture present, so it's very tolerable and much easier to do compared to an ice bath or cold shower. Towards the end of the treatment, you may get a "pins and needles" sensation that disappears immediately after the treatment.</p></div>

      <div class="faq__q"><svg viewBox="0 0 12 12"><path d="M2 3h8L6 10z" fill="#fff"/></svg>Is it safe?</div>
      <div class="faq__a"><p>Yes, the liquid nitrogen that is used as a chilling agent does not come into contact with your skin. Nitrogen is nontoxic and nonflammable; it comprises 78% of the air we breathe. A trained operator is always present during the treatment to control the temperature and monitor your comfort. There are no locks or latches on the door, so you are able to exit the cryochamber easily and quickly anytime.</p></div>

      <div class="faq__q"><svg viewBox="0 0 12 12"><circle cx="6" cy="2.5" r="1.6" fill="#fff"/><path d="M6 4v4M3 5l3 1 3-1M6 8l-2 3M6 8l2 3" fill="none" stroke="#fff" stroke-width="1.2"/></svg>How do I feel after a treatment?</div>
      <div class="faq__a"><p>The brisk exhilaration causes your brain to release high amounts of endorphin and norepinephrine, which make you feel good and focused. Most people report feeling energetic and full of life. The buoyant effects from each session peak after many hours and may last for weeks.</p></div>
    </div>

    <div class="faq__web">www.yourwebsite.com</div>
  </div>

  <div class="panel applications">
    <svg class="applications__wave" width="213" height="26" viewBox="0 0 213 26"><path d="M0 0H213V23C170 6 120-4 60 4C35 8 15 10 0 10Z" fill="#fff"/></svg>
    <div class="shot shot--knee" role="img" aria-label="Photo of a runner holding a sore knee at sunset"></div>
    <div class="blurb" style="left:7px;top:45px">Targeted cold exposure helps ease stiff joints and sore muscles so you can return to movement sooner with less discomfort.</div>
    <div class="shot shot--gym" role="img" aria-label="Photo of an athlete training in a gym"></div>
    <div class="blurb" style="left:108px;top:137px">Short sessions fit into busy training schedules and support faster recovery between workouts, games and long competitive seasons.</div>
    <div class="shot shot--road" role="img" aria-label="Photo of a runner's legs on an open road"></div>
    <div class="blurb" style="left:12px;top:236px">Runners and active people use regular treatments to reduce inflammation, recover from long distances and keep performing well.</div>
    <div class="applications__title">Application:</div>
    <ul class="applications__list">
      <li>Athletic Performance</li><li>Post-surgical Recovery</li><li>Musculosketetal Injuries</li><li>Rheumatoid Arthritis</li><li>Caloric Burn</li><li>Skin Disorders</li><li>Autoimmune</li><li>Other Inflammatory Disorders</li>
    </ul>
  </div>

  <div class="panel benefits">
    <div class="benefits__brand"><i></i><span>HARBOURLINE<br>COLDWORKS</span></div>
    <div class="benefits__title">Benefits:</div>
    <ul class="benefits__list">
      <li>Pain Management</li><li>Injury Therapy</li><li>Rapid Recovery</li><li>Performance</li><li>Metabolic Boost</li><li>Immunity Boost</li><li>Anti-Aging</li><li>Skin Rejevenation</li>
    </ul>
    <div class="benefits__machine" role="img" aria-label="Photo of the branded cryotherapy chamber in a treatment room"></div>
  </div>

  <div class="panel spine" style="width:80px">
    <div class="spine__mark"></div>
    <div class="spine__name">HARBOURLINE<br>COLDWORKS</div>
    <div class="spine__tag"><span class="spine__protocol">CUSTOMIZE TREATMENT PROTOCOL</span><br><span class="spine__minutes">JUST 3 MINUTE</span></div>
  </div>
</section>

</body>
</html>
```